Front cover for our tenth anniversary show programme

To create an eye catching tenth anniversary front cover for our programme

Moonbrook presents DANCE! 2015

date of the show Sunday 3rd May 2015

Venue The Harrowgate Stagehouse

please see the updated brief!

Reason: there hasn't been anything that is quite right

```html
<!DOCTYPE html>
<html lang="en">
<head>
<meta charset="utf-8">
<title>Moonbrook presents DANCE! 2015 – Programme Cover</title>
<link rel="stylesheet" href="https://fonts.googleapis.com/css2?family=Anton&family=Open+Sans:wght@400;700&display=swap">
<style>
  :root {
    --backdrop: #d9dadb;
    --cover-white: #ffffff;
    --band-dark: #262626;
    --band-darker: #1b1b1b;
    --text-light: #ffffff;
    --accent-pink: #e0368f;
    --photo-purple: #6a2f8f;
    --photo-red: #b8263f;
    --photo-blue: #2f3f9a;
    --photo-dark: #2a1a2e;
  }
  * { box-sizing: border-box; margin: 0; padding: 0; }
  html, body {
    width: 1200px;
    height: 850px;
    overflow: hidden;
    background: var(--backdrop);
  }
  .canvas {
    position: relative;
    width: 1200px;
    height: 850px;
    background: radial-gradient(ellipse at 50% 40%, #eeeeef 0%, var(--backdrop) 75%);
  }
  .programme-cover {
    position: absolute;
    left: 380px;
    top: 35px;
    width: 440px;
    height: 780px;
    background: var(--cover-white);
    box-shadow: 0 10px 30px rgba(0,0,0,0.18);
    overflow: hidden;
  }
  .cover-title {
    position: absolute;
    left: 0;
    top: 0;
    width: 440px;
    height: 512px;
  }
  .cover-title text {
    font-family: "Anton", "Oswald", sans-serif;
    text-transform: uppercase;
  }
  .info-band {
    position: absolute;
    left: 0;
    top: 512px;
    width: 100%;
    height: 268px;
    background: linear-gradient(180deg, var(--band-dark), var(--band-darker));
    font-family: "Open Sans", Arial, sans-serif;
  }
  .show-details {
    position: absolute;
    left: 26px;
    top: 108px;
    font-weight: 700;
    font-size: 14px;
    line-height: 1.4;
  }
  .show-date { color: var(--text-light); }
  .show-venue { color: var(--accent-pink); }
  .company-name {
    position: absolute;
    right: 28px;
    top: 116px;
    display: flex;
    align-items: center;
    gap: 10px;
    color: var(--text-light);
    font-weight: 700;
    font-size: 28px;
    line-height: 1;
  }
  .name-dot {
    width: 16px;
    height: 16px;
    border-radius: 50%;
    background: var(--accent-pink);
  }
</style>
</head>
<body>
  <main class="canvas">
    <section class="programme-cover">
      <svg class="cover-title" viewBox="0 0 440 512" role="img"
           aria-label="Title lettering filled with stage photographs of young dancers performing under purple, red and blue lights">
        <defs>
          <linearGradient id="stage-photo-fill" x1="0" y1="0" x2="1" y2="1">
            <stop offset="0" stop-color="var(--photo-blue)"/>
            <stop offset="0.25" stop-color="var(--photo-purple)"/>
            <stop offset="0.45" stop-color="var(--photo-red)"/>
            <stop offset="0.65" stop-color="var(--photo-dark)"/>
            <stop offset="0.82" stop-color="var(--photo-purple)"/>
            <stop offset="1" stop-color="var(--photo-red)"/>
          </linearGradient>
        </defs>
        <g fill="url(#stage-photo-fill)">
          <text x="48" y="147" font-size="74" textLength="344" lengthAdjust="spacingAndGlyphs">Moonbrook</text>
          <text x="48" y="223" font-size="80" textLength="344" lengthAdjust="spacingAndGlyphs">Presents</text>
          <text x="48" y="379" font-size="172" textLength="344" lengthAdjust="spacingAndGlyphs">Dance</text>
          <text x="48" y="509" font-size="143" textLength="344" lengthAdjust="spacingAndGlyphs">2015</text>
        </g>
      </svg>

      <footer class="info-band">
        <div class="show-details">
          <p class="show-date">3rd May 2015</p>
          <p class="show-venue">Harrowgate Stagehouse</p>
        </div>
        <p class="company-name"><span class="name-dot"></span>Moonbrook</p>
      </footer>
    </section>
  </main>
</body>
</html>
```